Termite Rack Card 4 x 9 or 3.5 x 8.5

You will see an older version of the HarborTermiteRack Card this will need to be modernized with the look and branding feel of the 2024HarborFlyer file that is attached.

Remove the following verbiage from the older version- FREE TERMITE INSPECTIONS- BEST PRICES SHOULD BE REPLACED WITH COMPETITIVE PRICES- Remove paragraph our 50 Certified Master inspectors and Our Harbor Group Termite Division provides Free... Remove we will beat any fumigation or legtimate repair.

The following verbiage on one side.

Protect your Client's greatest asset with a Pre-Listing Termite Inspection

Speed up the Sales Process - By having the seller conduct a termite inspection, you reduce the risk of delays or complications. With this essential step complete, you can expedite the transaction timeline and close deals faster!

Enhance Property Value - Uncovering and remedying termite problems early can prevent costly damages and preserve the integrity of the home. With a clean bill of health from a termite inspection, you can market the property with confidence!

Boost Buyer Confidence - A pre-listing termite inspection demonstrates proactive care for the property, instilling trust in potential buyers. Identifying issues upfront, you also eliminate surprises during negotiations, leading to smoother transactions and happier clients.

The Following Bullet points on the opposite side-
HARBOR GROUP
TERMITE SOLUTIONS

*Pre-Listing Inspections
*Inspection
*Treatment
*Repairs
*Fumigations
*Bill Repairs through Escrow
*Over 40 Years Experience
*Modern and effective treatmetns
*Quality and Integrity

```html
<!DOCTYPE html>
<html lang="en">
<head>
<meta charset="utf-8">
<title>Harbor Group Termite Rack Card</title>
<link rel="stylesheet" href="https://fonts.googleapis.com/css2?family=Open+Sans:wght@400;600;700;800&display=swap">
<style>
  :root {
    --blue: #1466b3;
    --blue-dark: #0d4f91;
    --sky: #d8e6f5;
    --grey-text: #5a5f66;
    --muted: #8e99a6;
    --card-grey: #d9d9d9;
    --red: #e02424;
    --black: #0b0b0b;
    --white: #ffffff;
    --stage: #e4e4e4;
  }
  * { box-sizing: border-box; margin: 0; padding: 0; }
  html, body { width: 1200px; height: 802px; overflow: hidden; }
  body {
    background: var(--stage);
    font-family: "Open Sans", Arial, sans-serif;
    position: relative;
  }
  ul { list-style: none; }
  .rack-card {
    position: absolute;
    top: 18px;
    width: 340px;
    height: 766px;
    overflow: hidden;
    box-shadow: 0 6px 18px rgba(0,0,0,.18);
  }
  .rack-card--front { left: 200px; background: linear-gradient(#ffffff 0%, #ffffff 12%, var(--sky) 34%); }
  .rack-card--back { left: 660px; background: var(--card-grey); }

  /* brand lockup */
  .brand { position: absolute; display: flex; align-items: center; gap: 8px; }
  .brand__dot { width: 46px; height: 46px; border-radius: 50%; background: var(--blue); flex: none; }
  .brand__name { font-weight: 800; font-size: 24px; color: var(--blue); letter-spacing: .5px; line-height: 1; }
  .brand__tag { font-weight: 600; font-size: 8px; color: var(--grey-text); letter-spacing: .6px; margin-top: 3px; }

  /* front */
  .front__brand { top: 36px; left: 30px; }
  .front__headline {
    position: absolute; top: 118px; left: 0; width: 100%;
    text-align: center; font-weight: 800; font-size: 14px; color: var(--grey-text);
  }
  .front__headline em { font-style: normal; color: var(--blue); }
  .front__with {
    display: flex; align-items: center; justify-content: center; gap: 8px;
    font-size: 8px; font-weight: 600; color: var(--muted); letter-spacing: 1px; margin-top: 2px;
  }
  .front__with::before, .front__with::after { content: ""; width: 36px; height: 1px; background: var(--muted); }
  .front__band {
    position: absolute; top: 156px; left: 22px; width: 308px; height: 36px;
    background: var(--blue); color: var(--white);
    clip-path: polygon(3% 0, 100% 0, 97% 100%, 0 100%);
    font-weight: 800; font-size: 16px; text-align: center; line-height: 36px;
  }
  .front__photo {
    position: absolute; top: 210px; left: 0; width: 100%; height: 370px;
    background: linear-gradient(#b9cfe6 0%, #8a7464 45%, #6f5a4a 75%, #5d5d5d 100%);
  }
  .front__panel {
    position: absolute; top: 452px; left: 26px; width: 296px; height: 282px;
    background: var(--blue); color: var(--white); padding: 46px 14px 0 14px;
  }
  .benefit { display: flex; gap: 8px; margin-bottom: 10px; }
  .benefit__icon { width: 26px; height: 26px; background: rgba(255,255,255,.35); border-radius: 4px; flex: none; margin-top: 16px; }
  .benefit__title { font-weight: 800; font-size: 10px; margin-bottom: 2px; }
  .benefit__text { font-size: 8px; line-height: 1.3; }
  .ribbon {
    position: absolute; left: 4px; top: 472px; width: 196px; height: 26px;
    background: var(--red); color: var(--white); font-weight: 800; font-size: 14px;
    text-align: center; line-height: 26px;
    transform-origin: left bottom; transform: rotate(-22deg);
  }
  .footer {
    position: absolute; bottom: 0; left: 0; width: 100%; height: 32px;
    background: var(--black); color: var(--white);
    display: flex; align-items: center; justify-content: center; gap: 12px;
    font-weight: 700; font-size: 11.5px;
  }
  .footer__item { display: flex; align-items: center; gap: 5px; }
  .footer svg { width: 13px; height: 13px; }

  /* back */
  .back__top { position: absolute; top: 0; left: 0; width: 100%; height: 140px; }
  .back__brand { top: 28px; left: 26px; }
  .back__band {
    position: absolute; top: 155px; left: 10px; width: 320px; height: 32px;
    background: var(--blue); color: var(--white);
    clip-path: polygon(2% 0, 100% 0, 98% 100%, 0 100%);
    font-weight: 800; font-size: 21px; text-align: center; line-height: 32px;
  }
  .solution {
    position: absolute; border: 1.5px solid var(--blue); border-radius: 2px;
    background: rgba(255,255,255,.25); color: var(--blue);
    font-weight: 800; font-size: 14px; line-height: 1.05; padding: 3px 6px;
  }
  .back__photo {
    position: absolute; left: 20px; top: 530px; width: 320px; height: 205px;
    background: linear-gradient(160deg, rgba(217,217,217,0) 0%, #cfcfcf 35%, #f2f2f2 70%, #bdbdbd 100%);
  }
</style>
</head>
<body>

<section class="rack-card rack-card--front">
  <div class="brand front__brand">
    <span class="brand__dot"></span>
    <div>
      <div class="brand__name">HARBOR GROUP</div>
      <div class="brand__tag">INSPECTION PROFESSIONALS</div>
    </div>
  </div>

  <div class="front__photo" role="img" aria-label="Photo of a two-storey brick house with double garage under a blue sky"></div>

  <h1 class="front__headline">PROTECT YOUR <em>CLIENT'S GREATEST ASSET</em><span class="front__with">WITH A</span></h1>
  <div class="front__band">PRE-LISTING TERMITE INSPECTION</div>

  <div class="front__panel">
    <div class="benefit">
      <span class="benefit__icon" role="img" aria-label="Icon of a person moving quickly"></span>
      <div>
        <h2 class="benefit__title">SPEED UP THE SALES PROCESS</h2>
        <p class="benefit__text">By having the seller conduct a termite inspection, you reduce the risk of delays or complications. With this essential step complete, you can expedite the transaction timeline and close deals faster!</p>
      </div>
    </div>
    <div class="benefit">
      <span class="benefit__icon" role="img" aria-label="Icon of a hand holding a house and value symbols"></span>
      <div>
        <h2 class="benefit__title">ENHANCE PROPERTY VALUE</h2>
        <p class="benefit__text">Uncovering and remedying termite problems early can prevent costly damages and preserve the integrity of the home. With a clean bill of health from a termite inspection, you can market the property with confidence!</p>
      </div>
    </div>
    <div class="benefit">
      <span class="benefit__icon" role="img" aria-label="Icon of a buyer with a checklist"></span>
      <div>
        <h2 class="benefit__title">BOOST BUYER CONFIDENCE</h2>
        <p class="benefit__text">A pre-listing termite inspection demonstrates proactive care for the property, instilling trust in potential buyers. Identifying issues upfront, you also eliminate surprises during negotiations, leading to smoother transactions and happier clients.</p>
      </div>
    </div>
  </div>

  <div class="ribbon">COMPETITIVE PRICES</div>

  <footer class="footer">
    <span class="footer__item">
      <svg viewBox="0 0 24 24"><path fill="#fff" d="M6.6 10.8a15 15 0 0 0 6.6 6.6l2.2-2.2a1 1 0 0 1 1-.25 11.4 11.4 0 0 0 3.6.57 1 1 0 0 1 1 1V20a1 1 0 0 1-1 1A17 17 0 0 1 3 4a1 1 0 0 1 1-1h3.5a1 1 0 0 1 1 1c0 1.250.2 2.45.57 3.57a1 1 0 0 1-.25 1z"/></svg>
      1-800-555-0147
    </span>
    <span class="footer__item">
      <svg viewBox="0 0 24 24" fill="none" stroke="#fff" stroke-width="2"><circle cx="12" cy="12" r="9"/><path d="M3 12h18M12 3c3 3 3 15 0 18M12 3c-3 3-3 15 0 18"/></svg>
      HarborInspections.com
    </span>
  </footer>
</section>

<section class="rack-card rack-card--back">
  <svg class="back__top" viewBox="0 0 340 140" preserveAspectRatio="none" aria-hidden="true">
    <path d="M0 0H340V80C270 150 150 140 70 120C40 112 15 100 0 80Z" fill="#ffffff"/>
  </svg>
  <div class="brand back__brand">
    <span class="brand__dot"></span>
    <div>
      <div class="brand__name">HARBOR GROUP</div>
      <div class="brand__tag">INSPECTION PROFESSIONALS</div>
    </div>
  </div>

  <h1 class="back__band">TERMITE SOLUTIONS</h1>

  <div class="back__photo" role="img" aria-label="Photo of a white modern apartment building with balconies"></div>

  <ul>
    <li class="solution" style="left:58px;top:228px;">Pre-Listing<br>Inspections</li>
    <li class="solution" style="left:171px;top:277px;">Inspection</li>
    <li class="solution" style="left:35px;top:298px;">Treatment</li>
    <li class="solution" style="left:188px;top:318px;">Repairs</li>
    <li class="solution" style="left:53px;top:342px;">Fumigations</li>
    <li class="solution" style="left:188px;top:358px;">Bill Repairs<br>through Escrow</li>
    <li class="solution" style="left:35px;top:398px;">Over 40 Years<br>Experience</li>
    <li class="solution" style="left:180px;top:434px;">Modern and<br>effective<br>treatments</li>
    <li class="solution" style="left:48px;top:489px;">Quality and<br>Integrity</li>
  </ul>

  <footer class="footer">
    <span class="footer__item">
      <svg viewBox="0 0 24 24"><path fill="#fff" d="M6.6 10.8a15 15 0 0 0 6.6 6.6l2.2-2.2a1 1 0 0 1 1-.25 11.4 11.4 0 0 0 3.6.57 1 1 0 0 1 1 1V20a1 1 0 0 1-1 1A17 17 0 0 1 3 4a1 1 0 0 1 1-1h3.5a1 1 0 0 1 1 1c0 1.25.2 2.45.57 3.57a1 1 0 0 1-.25 1z"/></svg>
      1-800-555-0147
    </span>
    <span class="footer__item">
      <svg viewBox="0 0 24 24" fill="none" stroke="#fff" stroke-width="2"><circle cx="12" cy="12" r="9"/><path d="M3 12h18M12 3c3 3 3 15 0 18M12 3c-3 3-3 15 0 18"/></svg>
      HarborInspections.com
    </span>
  </footer>
</section>

</body>
</html>
```